Natural Cosmetics need a Packaging Design

We need a PACKAGING design for labels on hand/body wash bottles and soap paper boxes.
We target at high end markets.
We expect a contemporary and trendy design.
We don't need a separate logo. The brand name "Va Mirel" acts as the logo.
We want a modern and classic font for "Va Mirel".
Please see attached pictures for packaging samples.

Industry/Entity Type

Cosmetics

Requirements
Should not have
• a separate logo from the brand name

```html
<!DOCTYPE html>
<html lang="en">
<head>
<meta charset="utf-8">
<title>Va Mirel – Moisturizing Hand Soap Labels</title>
<link rel="stylesheet" href="https://fonts.googleapis.com/css2?family=Arimo:wght@400;700&display=swap">
<style>
  :root {
    --canvas: #ffffff;
    --leaf-green: #13a84a;
    --band-light: #c6e36a;
    --glow-centre: #fbfbd8;
    --glow-mid: #e4ef8c;
    --glow-edge: #9ccc3a;
    --ink: #1c1c1c;
    --badge-green: #16a54c;
    --badge-pink: #e6147e;
    --badge-rim: #c9e58a;
    --white: #ffffff;
  }
  html, body {
    margin: 0;
    width: 1200px;
    height: 764px;
    overflow: hidden;
    background: var(--canvas);
  }
  .sheet { display: block; width: 1200px; height: 764px; }
  .brand-name { font-family: "Arimo", sans-serif; font-weight: 400; font-size: 60px; fill: var(--white); letter-spacing: 2px; }
  .tagline { font-family: "Arimo", sans-serif; font-size: 24px; fill: var(--ink); letter-spacing: 1px; }
  .flavour { font-family: "Arimo", sans-serif; font-weight: 700; font-size: 36px; fill: var(--white); }
  .volume { font-family: "Arimo", sans-serif; font-size: 20px; fill: var(--ink); }
</style>
</head>
<body>
<svg class="sheet" viewBox="0 0 1200 764" xmlns="http://www.w3.org/2000/svg">
  <defs>
    <radialGradient id="glow-left" cx="0.45" cy="0.45" r="0.75">
      <stop offset="0" stop-color="var(--glow-centre)"/>
      <stop offset="0.5" stop-color="var(--glow-mid)"/>
      <stop offset="1" stop-color="var(--glow-edge)"/>
    </radialGradient>
    <radialGradient id="glow-right" cx="0.5" cy="0.4" r="0.8">
      <stop offset="0" stop-color="var(--glow-centre)"/>
      <stop offset="0.45" stop-color="var(--glow-mid)"/>
      <stop offset="1" stop-color="var(--glow-edge)"/>
    </radialGradient>
    <linearGradient id="band-fade" x1="0" y1="0" x2="0" y2="1">
      <stop offset="0" stop-color="var(--leaf-green)"/>
      <stop offset="0.75" stop-color="var(--leaf-green)"/>
      <stop offset="1" stop-color="#6cc23a"/>
    </linearGradient>
    <clipPath id="clip-rect-label"><rect x="45" y="48" width="538" height="657"/></clipPath>
    <clipPath id="clip-round-label"><rect x="690" y="50" width="475" height="652" rx="66"/></clipPath>
  </defs>

  <!-- Rectangular label -->
  <g class="label label--rect" clip-path="url(#clip-rect-label)">
    <rect class="label__photo" x="45" y="48" width="538" height="657" fill="url(#glow-left)" role="img" aria-label="Photo of a woman in a towel touching her face, with green leaves on a soft yellow-green glow"/>
    <path class="label__band-light" d="M45,270 C150,258 230,318 330,318 C430,318 500,300 583,350 V48 H45 Z" fill="var(--band-light)"/>
    <path class="label__band" d="M45,258 C150,246 230,302 330,302 C430,302 500,285 583,332 V48 H45 Z" fill="url(#band-fade)"/>
    <text class="brand-name" x="315" y="195" text-anchor="middle">VA MIREL</text>
    <text class="tagline" x="315" y="235" text-anchor="middle">Moisturizing hand Soap</text>
    <ellipse class="badge" cx="204" cy="524" rx="88" ry="58" fill="var(--badge-green)" stroke="var(--badge-rim)" stroke-width="3" transform="rotate(-12 204 524)"/>
    <text class="flavour" x="206" y="513" text-anchor="middle" transform="rotate(-10 206 513)">Harbal</text>
    <text class="flavour" x="210" y="553" text-anchor="middle" transform="rotate(-10 210 553)">Lime</text>
    <text class="volume" x="312" y="668" text-anchor="middle">12FL OZ</text>
  </g>

  <!-- Rounded label -->
  <g class="label label--round" clip-path="url(#clip-round-label)">
    <rect class="label__photo" x="690" y="50" width="475" height="652" fill="url(#glow-right)" role="img" aria-label="Photo of green tea leaves on a soft yellow-green glow"/>
    <path class="label__band-light" d="M690,285 C790,275 860,332 950,332 C1040,332 1100,300 1165,325 V50 H690 Z" fill="var(--band-light)"/>
    <path class="label__band" d="M690,272 C790,262 860,318 950,318 C1040,318 1100,287 1165,308 V50 H690 Z" fill="url(#band-fade)"/>
    <text class="brand-name" x="925" y="195" text-anchor="middle">VA MIREL</text>
    <text class="tagline" x="925" y="235" text-anchor="middle">Moisturizing hand Soap</text>
    <ellipse class="badge" cx="1010" cy="456" rx="92" ry="58" fill="var(--badge-pink)" stroke="var(--badge-rim)" stroke-width="3" transform="rotate(-10 1010 456)"/>
    <text class="flavour" x="1010" y="446" text-anchor="middle" transform="rotate(-8 1010 446)">Harbal</text>
    <text class="flavour" x="1014" y="486" text-anchor="middle" transform="rotate(-8 1014 486)">Lime</text>
    <text class="volume" x="925" y="670" text-anchor="middle">12FL OZ</text>
  </g>
</svg>
</body>
</html>
```